Logo + Label Design (Men’s Grooming Brand & Product Packaging)

Design a logo and 2 oz pomade label for Rook, a modern men’s grooming brand focused on clean, high-quality, natural ingredients. The design should establish a bold, masculine, minimalist identity that can later extend to products like shaving gel and body wash.

Key Requirements

Create a primary logo for “Rook” and a core label for the 2 oz pomade jar (screw-top).

Use a clean, modern style — masculine, confident, and approachable (think Milton’s, Velta, Northern Guild).

Design for 1–2 color screen printing on solid jar colors (white, black, or navy).

Avoid gradients, foil, or embossing. Must work in black & white.

Provide: vector logo, mockup of the 2 oz jar, color palette (CMYK/RGB/HEX), and font specs.

Winning design may lead to future projects (body wash, shave gel, skincare lines).

Font styles to use
Other font styles liked:
• We like the fonts and design concept in the attached mockup.

Requirements
Should not have
• We want to avoid too much writing or busy designs. We want to avoid having graphics/illustrations embedded in the logo if they will cause the brand to look less classy or sophisticated. We also want the design to look simple and all-American (e.g. Pemberton and Vale, Tall Pine, The LOFT, etc). We’d like to give a Halloway & Brinks vibe that feels classy and high end.

```html
<!DOCTYPE html>
<html lang="en">
<head>
<meta charset="utf-8">
<title>Rook Hair Pomade – 2 oz Labels</title>
<link href="https://fonts.googleapis.com/css2?family=Oswald:wght@400;500;600;700&family=Roboto+Condensed:wght@400;700&display=swap" rel="stylesheet">
<style>
  :root{
    --jar-black:#141414;
    --jar-white:#ffffff;
    --ink-white:#f4f4f4;
    --ink-black:#111111;
    --accent-blue:#1fb8ec;
    --accent-gold:#c9962e;
    --page:#ffffff;
    --muted-dark:#333333;
  }
  *{margin:0;padding:0;box-sizing:border-box}
  html,body{width:1200px;height:1200px;overflow:hidden;background:var(--page)}
  body{position:relative;font-family:"Oswald",sans-serif}

  /* lid labels */
  .lid{position:absolute;border-radius:50%;display:flex;flex-direction:column;align-items:center;text-align:center}
  .lid--black{background:var(--jar-black);color:var(--ink-white)}
  .lid--white{background:var(--jar-white);color:var(--ink-black);border:1px solid #e2e2e2}
  .lid-feature{left:620px;top:72px;width:494px;height:494px;padding-top:92px}
  .lid-small{width:362px;height:362px;padding-top:66px}
  .lid-small.is-left{left:200px;top:607px}
  .lid-small.is-right{left:638px;top:607px}

  .wordmark{font-family:"Oswald",sans-serif;font-weight:700;letter-spacing:2px;line-height:1}
  .lid-feature .wordmark{font-size:124px}
  .lid-small .wordmark{font-size:92px}
  .product-name{font-weight:500;letter-spacing:3px;line-height:1}
  .lid-feature .product-name{font-size:37px;margin-top:34px}
  .lid-small .product-name{font-size:27px;margin-top:24px}
  .scent{font-weight:500;line-height:1}
  .scent--blue{color:var(--accent-blue)}
  .scent--gold{color:var(--accent-gold)}
  .lid-feature .scent{font-size:24px;margin-top:18px}
  .lid-small .scent{font-size:15px;margin-top:13px}
  .hold{font-weight:400;letter-spacing:1px;line-height:1}
  .lid-feature .hold{font-size:17px;margin-top:16px}
  .lid-small .hold{font-size:12.5px;margin-top:12px}
  .net{font-weight:400;letter-spacing:1px;line-height:1.45}
  .lid-feature .net{font-size:16px;margin-top:30px}
  .lid-small .net{font-size:11.5px;margin-top:22px}

  /* side wrap bands */
  .wrap{position:absolute;overflow:hidden}
  .wrap--black{background:var(--jar-black);color:var(--ink-white)}
  .wrap--white{background:var(--jar-white);color:var(--ink-black);border:1px solid #e2e2e2}
  .wrap-feature{left:64px;top:210px;width:530px;height:300px}
  .wrap-small{top:990px;width:362px;height:170px}
  .wrap-small.is-left{left:200px}
  .wrap-small.is-right{left:638px}

  .claims{position:absolute;left:0;right:0;display:flex;justify-content:center;gap:8px;white-space:nowrap;font-family:"Oswald",sans-serif;font-weight:400;letter-spacing:.4px}
  .wrap-feature .claims{top:22px;font-size:9px}
  .wrap-small .claims{top:12px;font-size:7.6px}
  .seam{position:absolute;left:0;right:0;height:1px}
  .wrap--black .seam{background:var(--muted-dark)}
  .wrap--white .seam{background:#dcdcdc}
  .wrap-feature .seam{top:54px}
  .wrap-small .seam{top:32px}

  .panel{position:absolute;display:flex;align-items:center;justify-content:space-between}
  .panel > *{flex-shrink:0}
  .wrap-feature .panel{left:14px;right:14px;top:66px;bottom:10px}
  .wrap-small .panel{left:8px;right:8px;top:38px;bottom:6px}

  .directions{font-family:"Roboto Condensed",sans-serif;line-height:1.32}
  .wrap-feature .directions{width:140px;font-size:8.5px}
  .wrap-small .directions{width:90px;font-size:5.6px}
  .directions p+p{margin-top:7px}
  .maker{font-family:"Roboto Condensed",sans-serif;text-align:center;line-height:1.4}
  .wrap-feature .maker{width:88px;font-size:8.5px}
  .wrap-small .maker{width:64px;font-size:5.8px}
  .maker strong{display:block;font-weight:700;letter-spacing:.3px}
  .maker .visit{margin-top:8px}
  .side-mark{font-weight:700;line-height:1;letter-spacing:1px}
  .wrap--black .side-mark{color:#dedede}
  .wrap-feature .side-mark{font-size:66px}
  .wrap-small .side-mark{font-size:46px}
  .side-info{line-height:1.3;white-space:nowrap}
  .side-info .sn{font-weight:500;letter-spacing:1px}
  .wrap-feature .side-info{font-size:7.5px}
  .wrap-feature .side-info .sn{font-size:12px}
  .wrap-feature .side-info .scent{font-size:9px;margin:2px 0}
  .wrap-small .side-info{font-size:5.5px}
  .wrap-small .side-info .sn{font-size:8px}
  .wrap-small .side-info .scent{font-size:5.5px;margin:1px 0}
</style>
</head>
<body>

<!-- Fresh & Clean, black jar: side wrap -->
<section class="wrap wrap--black wrap-feature" aria-label="Side wrap label, black jar">
  <div class="claims"><span>NATURALLY DERIVED PLANT &amp; BEE-BASED INGREDIENTS</span><span>•</span><span>ALCOHOL FREE, NON-IRRITATING</span><span>•</span><span>FORMULATED TO MINIMIZE SCALP IRRITATION</span></div>
  <div class="seam"></div>
  <div class="panel">
    <div class="directions">
      <p>Warm a small amount of pomade between hands before massaging into damp hair (or dry hair for more texture). Style as desired. For external use only. Avoid eyes. If irritation occurs, discontinue use.</p>
      <p>Butyrospermum Parkii (Shea Butter), Cera Alba (Beeswax), Polyglycerol-3 Beeswax, Caprylic/Capric Triglyceride (Fractionated Coconut Oil), Fragrance (Parfum)</p>
    </div>
    <div class="maker"><strong>MANUFACTURED BY:</strong>Rook Health Products, Ashford, NC 27510<div class="visit">Visit us at<br>rookhealthproducts.com</div></div>
    <div class="side-mark">ROOK</div>
    <div class="side-info"><div class="sn">HAIR POMADE</div><div class="scent scent--blue">Fresh &amp; Clean</div><div>MEDIUM HOLD –<br>MATTE FINISH</div><div>NET WT 2 OZ (57 G)</div></div>
  </div>
</section>

<!-- Fresh & Clean, black jar: lid -->
<section class="lid lid--black lid-feature" aria-label="Lid label, black jar">
  <div class="wordmark">ROOK</div>
  <div class="product-name">HAIR POMADE</div>
  <div class="scent scent--blue">Fresh &amp; Clean</div>
  <div class="hold">MEDIUM HOLD – MATTE FINISH</div>
  <div class="net">NET WT<br>2 OZ (57 G)</div>
</section>

<!-- Fresh/Clean scents, white jar -->
<section class="lid lid--white lid-small is-left" aria-label="Lid label, white jar">
  <div class="wordmark">ROOK</div>
  <div class="product-name">HAIR POMADE</div>
  <div class="scent scent--gold">FOR FRESH/CLEAN SCENTS</div>
  <div class="hold">MEDIUM HOLD – MATTE FINISH</div>
  <div class="net">NET WT<br>2 OZ (57 G)</div>
</section>
<section class="wrap wrap--white wrap-small is-left" aria-label="Side wrap label, white jar">
  <div class="claims"><span>NATURALLY DERIVED PLANT &amp; BEE-BASED INGREDIENTS</span><span>•</span><span>ALCOHOL FREE, NON-IRRITATING</span></div>
  <div class="seam"></div>
  <div class="panel">
    <div class="directions"><p>Warm a small amount of pomade between hands before massaging into damp hair. Style as desired. If irritation occurs, discontinue use.</p><p>Shea Butter, Cera Alba (Beeswax), Polyglycerol-3, Caprylic/Capric Triglyceride, Fragrance (Parfum)</p></div>
    <div class="maker"><strong>MANUFACTURED BY:</strong>Rook Health Products, Ashford, NC 27510<div class="visit">Visit us at<br>rookhealthproducts.com</div></div>
    <div class="side-mark">ROOK</div>
    <div class="side-info"><div class="sn">HAIR POMADE</div><div class="scent scent--gold">FOR FRESH/CLEAN</div><div>MEDIUM HOLD</div><div>NET WT 2 OZ</div></div>
  </div>
</section>

<!-- Cologne/Evening, black jar -->
<section class="lid lid--black lid-small is-right" aria-label="Lid label, black jar, evening">
  <div class="wordmark">ROOK</div>
  <div class="product-name">HAIR POMADE</div>
  <div class="scent scent--blue">FOR COLOGNE/EVENING FRAGRANCES</div>
  <div class="hold">MEDIUM HOLD – MATTE FINISH</div>
  <div class="net">NET WT<br>2 OZ (57 G)</div>
</section>
<section class="wrap wrap--black wrap-small is-right" aria-label="Side wrap label, black jar, evening">
  <div class="claims"><span>NATURALLY DERIVED PLANT &amp; BEE-BASED INGREDIENTS</span><span>•</span><span>ALCOHOL FREE, NON-IRRITATING</span></div>
  <div class="seam"></div>
  <div class="panel">
    <div class="directions"><p>Warm a small amount of pomade between hands before massaging into damp hair. Style as desired. If irritation occurs, discontinue use.</p><p>Shea Butter, Cera Alba (Beeswax), Polyglycerol-3, Caprylic/Capric Triglyceride, Fragrance (Parfum)</p></div>
    <div class="maker"><strong>MANUFACTURED BY:</strong>Rook Health Products, Ashford, NC 27510<div class="visit">Visit us at<br>rookhealthproducts.com</div></div>
    <div class="side-mark">ROOK</div>
    <div class="side-info"><div class="sn">HAIR POMADE</div><div class="scent scent--blue">FOR COLOGNE/EVENING</div><div>MEDIUM HOLD</div><div>NET WT 2 OZ</div></div>
  </div>
</section>

</body>
</html>
```